Inspirational Quote Poster for Employees

For this project, we need a simple yet high-impact poster template that will be customized for each of our employees with a personalized inspirational quote and color scheme. This template should allow us to quickly and easily customize the text and colors in the poster without a lot of effort.

The poster design should consist of:
- A stylized text area to contain the main text of the quote
- A separate text area to contain the source of quote
- A background that complements the color and style of the text

Text may use different typographic effects (such as color, stroke weight, italicization, font size changes, drop shadows) to draw attention to words in the quote; the source of the quote may be formatted the same as the main text of the quote, or may be formatted differently to distinguish it from the main quote.

The background may be simply a single color, subtle texture, gradients, halftone effects, or other color/texture effects may be used to complement the text.

Examples of the types of posters envisioned by this project:
- http://www.tackvale.com/corwinpmaddox/artquarry-job-1/

Sample quotes to use to build your poster - choose whichever one you want, but be certain that the poster design will handle both long and short quotes:
- "Happiness in intelligent people is the rarest thing I know" - Bertram Faulconer
- "Wanting to be someone else is a waste of the person you are." - Miles Tavenor
- "Experience is not what happens to you. It is what you do with what happens to you." - Cyril Pembrage
- "Simplicity is the ultimate in sophistication." - Ottaviano Restelli
- "You will get all you want in life if you help enough other people get what they want." - Hap Dunmore
- "Hell, there are no rules here — we're trying to accomplish something." - Walter Brisbane

Quote

• Final deliverable must be:
• - Formatted for an 18” x 24” poster (in portrait orientation)
• - Delivered in Adobe InDesign, Adobe Illustrator, or Extended PostScript format
• - Use CMYK color mode
• - Be print-ready at 300dpi resolution
• - Include any fonts used in the template

```html
<!DOCTYPE html>
<html lang="en">
<head>
<meta charset="utf-8">
<title>Quote Poster</title>
<link rel="stylesheet" href="https://fonts.googleapis.com/css2?family=Barlow+Condensed:wght@400;600&display=swap">
<style>
  :root {
    --poster-yellow: #ffe200;
    --poster-yellow-deep: #fdd000;
    --poster-yellow-light: #fff01a;
    --ink: #0d0d0d;
  }
  html, body {
    margin: 0;
    padding: 0;
    overflow: hidden;
  }
  body {
    width: 849px;
    height: 1200px;
  }
  .poster {
    position: relative;
    width: 849px;
    height: 1200px;
    overflow: hidden;
    background-color: var(--poster-yellow);
    background-image:
      radial-gradient(ellipse 420px 260px at 18% 12%, var(--poster-yellow-light) 0%, transparent 70%),
      radial-gradient(ellipse 380px 300px at 82% 30%, var(--poster-yellow-deep) 0%, transparent 70%),
      radial-gradient(ellipse 460px 320px at 25% 62%, var(--poster-yellow-deep) 0%, transparent 72%),
      radial-gradient(ellipse 400px 280px at 78% 80%, var(--poster-yellow-light) 0%, transparent 70%),
      radial-gradient(ellipse 520px 300px at 40% 95%, var(--poster-yellow-deep) 0%, transparent 70%);
  }
  .quote {
    position: absolute;
    left: 97px;
    top: 367px;
    margin: 0;
    font-family: "Barlow Condensed", sans-serif;
    font-weight: 600;
    font-size: 78px;
    line-height: 84px;
    letter-spacing: 0.2px;
    text-transform: uppercase;
    color: var(--ink);
  }
  .quote-line {
    display: block;
    white-space: nowrap;
  }
  .quote-source {
    position: absolute;
    left: 97px;
    top: 708px;
    margin: 0;
    font-family: "Barlow Condensed", sans-serif;
    font-weight: 400;
    font-size: 42px;
    line-height: 50px;
    letter-spacing: 0.3px;
    text-transform: uppercase;
    color: var(--ink);
  }
</style>
</head>
<body>
  <main class="poster">
    <blockquote class="quote">
      <span class="quote-line">Happiness in</span>
      <span class="quote-line">intelligent people</span>
      <span class="quote-line">is the rarest thing</span>
      <span class="quote-line">I know</span>
    </blockquote>
    <p class="quote-source">Bertram Faulconer</p>
  </main>
</body>
</html>
```